Non-profit sports organization needs templates for Word and InDesign

"Fralo Teens" is a non-profit organization in Winterthur, which supports the recruitment of young talent by the handball clubs in Winterthur. Every year we run several camps, a tournament for schoolchildren and several handball lessons at school.
During these activities there are always written information. So far we have not given much thought to the design. But since we think that a professional design will also lead to more interaction, we now turn to you as a designer.

For the communication with partners, sponsors, patrons, etc. we need a uniform appearance. Since different departments are currently working with different programs, we need a template for letters and documentation for Word and InDesign.

We will need the documentation template for project descriptions, information, etc.
The letter templates are needed to contact sponsors, authorities, patrons, etc.

Both the letter template and the documentation template should look modern. The design should be based on the existing flyers. Otherwise we have no other requirements so far.

Homepage: www.fralo-teens.ch

Target Market(s)

Letters, documentation or information to authorities, sponsors, associations, patrons, members, participants, etc.

Requirements
Must have
• In addition to the design, the templates should also contain a concept for titles, paragraphs, lists, etc. (colors / fonts / ...)

Word and Indesign templates

```html
<!DOCTYPE html>
<html lang="en">
<head>
<meta charset="utf-8">
<title>Fralo Teens – Documentation Template</title>
<link href="https://fonts.googleapis.com/css2?family=Arimo:ital,wght@0,400;0,700;1,400&display=swap" rel="stylesheet">
<style>
  :root {
    --brand-red: #e3211b;
    --brand-blue: #3d9ad8;
    --ink: #111111;
    --paper: #ffffff;
    --rule: #222222;
    --player-fill: #e6eef4;
  }
  * { box-sizing: border-box; margin: 0; padding: 0; }
  html, body { width: 848px; height: 1200px; overflow: hidden; background: var(--paper); }
  body { font-family: "Arimo", Arial, sans-serif; color: var(--ink); }
  .page { position: relative; width: 848px; height: 1200px; overflow: hidden; }

  .header-rule { position: absolute; height: 2.5px; }
  .header-rule.red { top: 92px; background: var(--brand-red); }
  .header-rule.blue { top: 100px; background: var(--brand-blue); }
  .header-rule.left { left: 0; width: 348px; }
  .header-rule.right { left: 491px; right: 0; }

  .brand-name {
    position: absolute; top: 78px; left: 348px; width: 143px;
    text-align: center; font-size: 20px; font-weight: 700; color: var(--brand-blue);
    line-height: 36px;
  }

  .doc-title {
    position: absolute; top: 196px; left: 82px; width: 670px;
    text-align: center; font-size: 16.5px; font-weight: 700; color: var(--brand-blue);
  }

  .body-text { position: absolute; left: 82px; width: 670px; font-size: 14.2px; line-height: 17.2px; }
  .body-text p + p { margin-top: 4px; }
  .intro { top: 232px; }
  .feature-list { top: 563px; left: 120px; width: 400px; list-style: none; }
  .feature-list li { position: relative; padding-left: 19px; }
  .feature-list li::before {
    content: ""; position: absolute; left: 3px; top: 6px; width: 5px; height: 5px;
    border-radius: 50%; background: var(--brand-blue);
  }
  .quote { top: 680px; font-style: italic; }

  .data-table {
    position: absolute; top: 780px; left: 83px; width: 667px;
    border-collapse: collapse; font-size: 13px; table-layout: fixed;
  }
  .data-table th {
    background: var(--brand-blue); font-weight: 400; height: 20px; line-height: 19px;
    border: 1px solid var(--brand-blue); border-right-color: var(--rule); text-align: center;
  }
  .data-table th:last-child { border-right-color: var(--brand-blue); }
  .data-table td { border: 1px solid var(--rule); height: 21px; line-height: 19px; padding-left: 25px; }

  .closing { top: 882px; }
  .closing p { text-indent: 19px; }
  .closing p + p { margin-top: 17px; }
  .closing .tail { margin-top: 0; }

  .footer-rule { position: absolute; top: 1128px; left: 0; right: 0; height: 2.5px; background: var(--brand-red); }
  .player-badge {
    position: absolute; top: 1111px; width: 35px; height: 35px; border-radius: 50%;
    background: var(--player-fill); border: 1px solid var(--brand-blue);
  }
  .player-badge.first { left: 263px; }
  .player-badge.second { left: 592px; }
  .footer-item { position: absolute; top: 1136px; font-size: 14px; line-height: 17px; }
  .footer-item.address { left: 32px; }
  .footer-item.site { left: 372px; }
  .footer-item.mail { right: 32px; }
</style>
</head>
<body>
<main class="page">
  <div class="header-rule red left"></div>
  <div class="header-rule blue left"></div>
  <div class="header-rule red right"></div>
  <div class="header-rule blue right"></div>
  <div class="brand-name">Fralo Teens</div>

  <h1 class="doc-title">Lorem ipsum dolor sit amet</h1>

  <section class="body-text intro">
    <p>Lorem ipsum dolor sit amet, consectetur meri odipiscing elit Mauris pretium porta turpis, semper ornare magna elementum convallis.</p>
    <p>Aliquam malesuada dolor eros, nec fermentum massa commodo eu. NuLLa feLis purus, tincidunt nec uL&shy;trices a, dictum a mauris. Maecenas Lorem augue, pellentesque pulvinar quam a, pretium finibus magna. Quisque dapibus voLutpat massa nec vestibulum. Ut porttitor ultricies magna vitae iaculis.</p>
    <p>Suspendisse vel faucibus diam, dapibus peLLentesque quam. Maecenas eu varius nulla. PeLLentesque ornare tortor et pharetra peLLentesque. Nam in elementum ante.</p>
    <p>Nulla sodales eros et quam gravida molestie. Muspendisse sit amet pharetra dui.</p>
    <p>Quisque sit amet rhoncus dolor. Praesent euismod feLis nuLLa, sed sodales enim vehicula eu. Integer vestibuLum accumsan ligula, eget malesuada Lacus porttitor porta.</p>
    <p>Donee tincidunt enim et peLLentesque consequat. ALiquam vitae velit Lectus. Nam arcu vitae tortor Luctus, quis maLesuada metus rhoncus. Quisque ornare Lectus sed finibus condimentum. In at suscipit tortor, nec aLiquet est. Suspendisse potenti. Sed finibus veLit ipsum, a fermentum. PhaseLLus nec. Proin dignissim, nuLLa veL vehicuLa hendrerit, arcu urna sceLerisque nisL, non porta purus tortor in orci.</p>
    <p>Nulla lorem eros, hendrerit a mattis vel, elementum aliquam nisi. Etiam vel sapien mi. Cros nec varius ipsum. Interdum et malesuada fames ac ante ipsum primis in faucibus.</p>
  </section>

  <ul class="body-text feature-list">
    <li>Proin euismod lobortis lacinia.</li>
    <li>Proin euismod lobortis lacinia.</li>
    <li>Proin euismod lobortis lacinia.</li>
    <li>Proin euismod lobortis lacinia.</li>
    <li>Proin euismod lobortis lacinia.</li>
  </ul>

  <section class="body-text quote">
    <p>Etiam commodo, lacus enim lacinla lorem urna sit amet nibh.</p>
    <p>Aliquam malesuada dolor eros, nec fermentum massa commodo eu. NuLLa feLis purus, tincidunt nec uL&shy;trices a, dictum a mauris. Maecenas Lorem augue, pellentesque pulvinar quam a, pretium finibus magna. Quisque dapibus voLutpat massa nec vestibulum. Ut porttitor ultricies magna vitae iaculis.</p>
  </section>

  <table class="data-table">
    <thead>
      <tr><th>Nunc nec Leo</th><th>venenatis LiguLa</th><th>tempus Lectus</th><th>Proin faciLisis</th></tr>
    </thead>
    <tbody>
      <tr><td>Curabitur pretium</td><td>Curabitur pretium</td><td>Curabitur pretium</td><td>Curabitur pretium</td></tr>
      <tr><td>Curabitur pretium</td><td>Curabitur pretium</td><td>Curabitur pretium</td><td>Curabitur pretium</td></tr>
      <tr><td>Curabitur pretium</td><td>Curabitur pretium</td><td>Curabitur pretium</td><td>Curabitur pretium</td></tr>
    </tbody>
  </table>

  <section class="body-text closing">
    <p>Nunc nec Leo iaculis, venenatis LiguLa eget, tempus Lectus. Proin faciLisis eras a sapien sodaLes sodaLes. Curabitur pretium sed massa sed porta. NuLLa quis dui at risus uLtricies iacuLis. Curabitur vel tortor sagittis, Lobortis lacus pLacerat, euismod nibh. Class aptent taciti sociosqu ad Litora torquent per conubia nostra, per inceptos himenaeos. Integer sit amet dignissim mi.</p>
    <p>Nunc nec Leo iaculis, venenatis LiguLa eget, tempus Lectus. Proin faciLisis eras a sapien sodaLes sodaLes. Curabitur pretium sed massa sed porta. NuLLa quis dui at risus uLtricies iacuLis. Curabitur vel tortor sagittis, Lobortis lacus pLacerat, euismod nibh. Class aptent taciti sociosqu ad Litora torquent per conubia nostra, per inceptos himenaeos. Integer sit amet dignissim mi.</p>
    <p class="tail">conubia nostra, per inceptos himenaeos. Integer sit amet dignissim mi.</p>
  </section>

  <footer>
    <div class="footer-rule"></div>
    <div class="player-badge first" role="img" aria-label="Small round illustration of a handball player"></div>
    <div class="player-badge second" role="img" aria-label="Small round illustration of a handball player"></div>
    <div class="footer-item address">Fralo Teens 9100 Fralingen</div>
    <div class="footer-item site">https://www.fralo-teens.ch/</div>
    <div class="footer-item mail">info@fralo-teens.ch</div>
  </footer>
</main>
</body>
</html>
```